New Customers - Women's Apparel Postcard

We are in the process of buying a mailing list to try to get some new customers. We would like to entice them with a bunch of pictures of our clothing and a lucrative offer. I will attach some examples.
MAIN MESSAGE: We have great fashion for women of all ages & all sizes!
SECONDARY MESSAGE: Try us on, you are gonna love our great fashions:
OFFER: $10.00 off $20.00 purchase

Target Market(s)

45+ women

Industry/Entity Type

Womens Clothing

Requirements
Must have
• strong call to action

```html
<!DOCTYPE html>
<html lang="en">
<head>
<meta charset="utf-8">
<title>Maple Hour – New Customer Postcard</title>
<link rel="stylesheet" href="https://fonts.googleapis.com/css2?family=Oswald:wght@300;400;600&family=Great+Vibes&family=Libre+Baskerville&display=swap">
<style>
  :root {
    --paper: #fdfefe;
    --frame: #2a2420;
    --ribbon: #ff1a40;
    --ink: #111111;
    --white: #ffffff;
    --pink: #f47bbf;
    --cyan: #18d2f2;
    --blue: #6e98f6;
    --coral: #f6707a;
    --dress: #ff1a40;
  }
  * { margin: 0; padding: 0; box-sizing: border-box; }
  html, body { width: 1200px; height: 773px; overflow: hidden; background: var(--paper); }
  .postcard { position: relative; width: 1200px; height: 773px; background: var(--paper); overflow: hidden; }
  .card-frame { position: absolute; left: 16px; top: 12px; width: 1172px; height: 743px; border: 5px solid var(--frame); }
  .wash { position: absolute; left: 0; top: 0; }
  .offer-ribbon { position: absolute; left: 22px; top: 16px; }
  .offer-label {
    position: absolute; left: 23px; top: 20px;
    font-family: "Oswald", sans-serif; font-weight: 300; font-size: 34px; line-height: 1;
    letter-spacing: -1.5px; color: var(--white); white-space: nowrap;
  }
  .offer-amount {
    position: absolute; left: 117px; top: 20px;
    font-family: "Oswald", sans-serif; font-weight: 300; font-size: 34px; line-height: 1;
    letter-spacing: -1.5px; color: var(--ink); white-space: nowrap;
  }
  .offer-purchase {
    position: absolute; left: 113px; top: 50px;
    font-family: "Oswald", sans-serif; font-weight: 300; font-size: 64px; line-height: 1;
    letter-spacing: -1px; color: var(--ink);
  }
  .tagline {
    position: absolute; left: 0; top: 178px;
    font-family: "Great Vibes", cursive; font-size: 50px; line-height: 58px;
    letter-spacing: 2px; color: var(--white); white-space: nowrap;
  }
  .tagline span { display: block; }
  .tagline .l1 { padding-left: 336px; }
  .tagline .l2 { padding-left: 264px; }
  .tagline .l3 { padding-left: 304px; }
  .dress-art { position: absolute; left: 116px; top: 136px; }
  .brand-name {
    position: absolute; left: 124px; top: 482px;
    font-family: "Oswald", sans-serif; font-weight: 600; font-size: 74px; line-height: 1;
    color: var(--ink); letter-spacing: 1px; white-space: nowrap;
  }
  .brand-rule { position: absolute; left: 128px; top: 589px; width: 354px; height: 2px; background: var(--ink); }
  .brand-web {
    position: absolute; left: 130px; top: 595px;
    font-family: "Libre Baskerville", serif; font-size: 17px; letter-spacing: 5px; color: var(--ink); white-space: nowrap;
  }
  .main-message {
    position: absolute; left: 130px; top: 634px;
    font-family: "Oswald", sans-serif; font-weight: 300; font-size: 24px; line-height: 1.2;
    color: var(--ink); white-space: nowrap;
  }
  .call-to-action {
    position: absolute; left: 130px; top: 670px;
    font-family: "Oswald", sans-serif; font-weight: 400; font-size: 22px; line-height: 1.2;
    color: var(--ribbon); letter-spacing: 0.5px; white-space: nowrap;
  }
  .stamp-box { position: absolute; left: 1038px; top: 22px; width: 136px; height: 134px; border: 4px dashed var(--white); border-radius: 3px; }
</style>
</head>
<body>
<main class="postcard">

  <svg class="wash" width="1200" height="773" viewBox="0 0 1200 773" role="img" aria-label="Watercolour splashes in pink, turquoise, periwinkle and coral">
    <defs>
      <filter id="soft" x="-30%" y="-30%" width="160%" height="160%"><feGaussianBlur stdDeviation="14"/></filter>
      <radialGradient id="g-pink"><stop offset="0" stop-color="var(--pink)"/><stop offset="1" stop-color="var(--pink)" stop-opacity="0.45"/></radialGradient>
      <radialGradient id="g-cyan"><stop offset="0" stop-color="var(--cyan)"/><stop offset="1" stop-color="var(--cyan)" stop-opacity="0.7"/></radialGradient>
      <radialGradient id="g-blue"><stop offset="0" stop-color="var(--blue)"/><stop offset="1" stop-color="var(--blue)" stop-opacity="0.6"/></radialGradient>
      <radialGradient id="g-coral"><stop offset="0" stop-color="#f2385e"/><stop offset="1" stop-color="var(--coral)" stop-opacity="0.7"/></radialGradient>
    </defs>
    <g filter="url(#soft)">
      <ellipse cx="360" cy="300" rx="130" ry="160" fill="url(#g-pink)"/>
      <ellipse cx="560" cy="290" rx="150" ry="150" fill="url(#g-cyan)"/>
      <ellipse cx="520" cy="490" rx="150" ry="95" fill="url(#g-blue)"/>
      <ellipse cx="1070" cy="110" rx="150" ry="135" fill="url(#g-coral)"/>
    </g>
  </svg>

  <div class="card-frame"></div>

  <svg class="offer-ribbon" width="92" height="140" viewBox="0 0 92 140" aria-hidden="true">
    <polygon points="0,0 92,0 92,140 47,92 0,140" fill="var(--ribbon)"/>
  </svg>
  <div class="offer-label">OFFER:</div>
  <div class="offer-amount">$10.00 off $20.00</div>
  <div class="offer-purchase">Purchase</div>

  <svg class="dress-art" width="126" height="344" viewBox="0 0 126 344" role="img" aria-label="Fashion sketch of a red strapless dress on a figure">
    <rect x="0" y="0" width="126" height="344" rx="6" fill="var(--dress)"/>
  </svg>

  <p class="tagline">
    <span class="l1">Try us on,</span>
    <span class="l2">You are gonna love</span>
    <span class="l3">Great Fashion</span>
  </p>

  <div class="brand-name">MAPLE HOUR</div>
  <div class="brand-rule"></div>
  <div class="brand-web">www.maplehourdirect.com</div>

  <p class="main-message">Great fashion for women of all ages &amp; all sizes!</p>
  <p class="call-to-action">Bring this card in or shop online today – save $10 on $20!</p>

  <div class="stamp-box" aria-label="Stamp area"></div>
</main>
</body>
</html>
```